Business Card Design

Kitchen Cabinet company in Colorado. We recently changed our logo the use the colors grey and blue. Our company motto is "where ideas come to life" Wanting a business card to pop and stand out. I attached our new logo and colors scheme

Industry/Entity Type

Business

```html
<!DOCTYPE html>
<html lang="en">
<head>
<meta charset="utf-8">
<title>Cedar and Basin Works — Business Card</title>
<link rel="stylesheet" href="https://fonts.googleapis.com/css2?family=Cinzel:wght@400;700&display=swap">
<style>
  :root {
    --paper: #ffffff;
    --brand-blue: #2d6cb0;
    --deep-slate: #353b45;
    --card-grey: #d9dde2;
    --ink-navy: #1c2738;
    --light-text: #ffffff;
    --portrait-tone: #d4d8dd;
    --portrait-shade: #4a5260;
  }
  html, body {
    margin: 0;
    padding: 0;
    overflow: hidden;
    background: var(--paper);
  }
  .canvas {
    position: relative;
    width: 1200px;
    height: 900px;
    overflow: hidden;
    background: var(--paper);
    font-family: "Cinzel", serif;
    color: var(--ink-navy);
  }
  .header-band {
    position: absolute;
    left: 0; top: 114px;
    width: 1200px; height: 260px;
    background: var(--brand-blue);
  }
  .base-band {
    position: absolute;
    left: 0; top: 374px;
    width: 1200px; height: 394px;
    background: var(--deep-slate);
  }
  .card-panel {
    position: absolute;
    left: 218px; top: 374px;
    width: 754px; height: 394px;
    background: var(--card-grey);
    box-shadow: 0 0 28px rgba(0, 0, 0, 0.5);
  }
  .company-name {
    position: absolute;
    left: 0; top: 136px;
    width: 1200px;
    margin: 0;
    text-align: center;
    font-weight: 400;
    font-size: 46px;
    line-height: 1;
    color: var(--light-text);
  }
  .motto {
    position: absolute;
    left: 0; top: 198px;
    width: 1200px;
    margin: 0;
    text-align: center;
    font-weight: 400;
    font-size: 22px;
    line-height: 1;
    letter-spacing: 2px;
    color: var(--light-text);
  }
  .portrait-frame {
    position: absolute;
    left: 476px; top: 250px;
    width: 240px; height: 240px;
  }
  .holder-name {
    position: absolute;
    left: 218px; top: 502px;
    width: 754px;
    margin: 0;
    text-align: center;
    font-weight: 700;
    font-size: 40px;
    line-height: 1;
  }
  .holder-role {
    position: absolute;
    left: 218px; top: 550px;
    width: 754px;
    margin: 0;
    text-align: center;
    font-weight: 700;
    font-size: 26px;
    line-height: 1;
  }
  .social-dots {
    position: absolute;
    left: 520px; top: 598px;
    width: 152px;
    display: grid;
    grid-template-columns: repeat(4, 28px);
    gap: 6px 10px;
    justify-content: center;
  }
  .social-dot {
    width: 28px; height: 28px;
    border-radius: 50%;
    background: var(--brand-blue);
  }
  .handle-rule {
    position: absolute;
    left: 528px; top: 668px;
    width: 140px; height: 3px;
    background: var(--ink-navy);
  }
  .handle {
    position: absolute;
    left: 218px; top: 678px;
    width: 754px;
    margin: 0;
    text-align: center;
    font-weight: 700;
    font-size: 22px;
    line-height: 1;
    letter-spacing: 1px;
  }
</style>
</head>
<body>
  <main class="canvas">
    <div class="header-band"></div>
    <div class="base-band"></div>
    <section class="card-panel"></section>

    <h1 class="company-name">CEDAR AND BASIN WORKS</h1>
    <p class="motto">WHERE IDEAS COME TO LIFE</p>

    <svg class="portrait-frame" viewBox="0 0 240 240" xmlns="http://www.w3.org/2000/svg">
      <defs>
        <linearGradient id="portrait-fill" x1="0" y1="0" x2="0" y2="1">
          <stop offset="0" stop-color="#d4d8dd"/>
          <stop offset="1" stop-color="#4a5260"/>
        </linearGradient>
      </defs>
      <circle cx="120" cy="120" r="116" fill="#ffffff" stroke="#1c2738" stroke-width="8" stroke-dasharray="22 8"/>
      <circle cx="120" cy="120" r="104" fill="url(#portrait-fill)" role="img" aria-label="Portrait photo of the card holder in a suit"/>
    </svg>

    <h2 class="holder-name">OMAR HADDAD</h2>
    <p class="holder-role">GRAPHIC DESIGNER</p>

    <div class="social-dots" aria-hidden="true">
      <span class="social-dot"></span><span class="social-dot"></span>
      <span class="social-dot"></span><span class="social-dot"></span>
      <span class="social-dot"></span><span class="social-dot"></span>
      <span class="social-dot"></span><span class="social-dot"></span>
    </div>

    <div class="handle-rule"></div>
    <p class="handle">OMARWORKS</p>
  </main>
</body>
</html>
```